Fashion Design Business Card

I need a new business card designed for a new fashion company. I have attached what I have currently designed. I want it more feminine looking, the logo needs to be gold. I want it simple, feminine and stylish. Please give me some different ideas with the fonts.
Updates

I need to send the design we currently have, as we have worked out the logo.
You also need all of our details
Industry/Entity Type
Fashion
Look and feel
Each slider illustrates characteristics of the customer's brand and the style your logo design should communicate.

```html
<!DOCTYPE html>
<html lang="en">
<head>
<meta charset="utf-8">
<title>Marisa Holloway – Business Card</title>
<link rel="stylesheet" href="https://fonts.googleapis.com/css2?family=Cinzel:wght@400&family=Arimo:wght@400&display=swap">
<style>
  :root {
    --backdrop: #c8a272;
    --card-front: #6a4a38;
    --card-front-light: #7a5846;
    --card-back: #432e22;
    --card-back-glow: #6c5140;
    --panel: rgba(52, 34, 26, 0.82);
    --gold: #f2ae1c;
    --ivory: #f4ece4;
    --decor: rgba(70, 46, 34, 0.45);
  }
  * { margin: 0; padding: 0; box-sizing: border-box; }
  html, body { width: 1200px; height: 900px; overflow: hidden; }
  body {
    background: var(--backdrop);
    position: relative;
    font-family: "Arimo", Arial, sans-serif;
  }
  .card {
    position: absolute;
    left: 266px;
    width: 676px;
    height: 384px;
    overflow: hidden;
    box-shadow: 0 4px 14px rgba(40, 24, 12, 0.45);
  }
  .card--front {
    top: 44px;
    background: linear-gradient(100deg, var(--card-front) 40%, var(--card-front-light) 75%, var(--card-front) 100%);
  }
  .card--back {
    top: 470px;
    background: radial-gradient(ellipse 55% 70% at 50% 38%, var(--card-back-glow) 0%, var(--card-back) 75%);
  }
  .front-decor {
    position: absolute;
    left: 350px;
    top: 20px;
    width: 330px;
    height: 340px;
  }
  .info-panel {
    position: absolute;
    left: 0;
    top: 122px;
    width: 310px;
    height: 148px;
    background: var(--panel);
    padding: 14px 0 0 54px;
  }
  .info-panel__name {
    font-family: "Cinzel", Georgia, serif;
    font-weight: 400;
    font-size: 22px;
    letter-spacing: 0.5px;
    color: var(--gold);
    line-height: 1.1;
  }
  .info-panel__role {
    font-family: "Cinzel", Georgia, serif;
    font-size: 14px;
    color: var(--ivory);
    margin-top: 4px;
    letter-spacing: 0.5px;
  }
  .info-panel__contacts {
    list-style: none;
    margin-top: 16px;
    font-size: 11px;
    line-height: 1.65;
    color: var(--ivory);
  }
  .brand-dot {
    position: absolute;
    left: 50%;
    top: 104px;
    width: 110px;
    height: 110px;
    margin-left: -55px;
    border-radius: 50%;
    background: var(--gold);
  }
  .back-name {
    position: absolute;
    left: 0;
    right: 0;
    top: 262px;
    text-align: center;
    font-family: "Cinzel", Georgia, serif;
    font-weight: 400;
    font-size: 29px;
    letter-spacing: 2px;
    color: var(--gold);
  }
</style>
</head>
<body>
  <section class="card card--front" aria-label="Business card front">
    <svg class="front-decor" viewBox="0 0 330 340" aria-hidden="true">
      <circle cx="175" cy="170" r="160" fill="var(--decor)"/>
    </svg>
    <div class="info-panel">
      <h1 class="info-panel__name">MARISA HOLLOWAY</h1>
      <p class="info-panel__role">FASHION DESIGNER</p>
      <ul class="info-panel__contacts">
        <li>P&nbsp;: 0400 312 774</li>
        <li>E&nbsp;: marisa@marisaholloway.com</li>
        <li>www.marisaholloway.com</li>
      </ul>
    </div>
  </section>

  <section class="card card--back" aria-label="Business card back">
    <span class="brand-dot" aria-hidden="true"></span>
    <p class="back-name">MARISA HOLLOWAY</p>
  </section>
</body>
</html>
```